Covid 19 Exit Strategy one page brochure

I would like to design, and will need URGENT help, a brochure detailing a Covid 19 Exit Strategy plan. This brochure will need to be understood easily and the graphics inside should make it easy for people to understand without reading the entire text. This project is quite urgent and needs to be completed THIS WEEK - by Saturday may 16th at the latest. I am attaching two examples. I will provide the text.

```html
<!DOCTYPE html>
<html lang="en">
<head>
<meta charset="utf-8">
<title>Exit Strategy Plan</title>
<link href="https://fonts.googleapis.com/css2?family=Montserrat:wght@500;700;800&display=swap" rel="stylesheet">
<style>
  :root{
    --stage:#6b6c70;
    --navy:#33475e;
    --aqua:#93d5e2;
    --aqua-soft:#bfe4ee;
    --aqua-title:#8fd7e3;
    --slate:#5b7a8c;
    --slate-light:#7fa3b2;
    --paper-edge:#dfe3e7;
    --white:#ffffff;
  }
  html,body{margin:0;padding:0;overflow:hidden}
  body{width:1200px;height:2646px;background:var(--stage);position:relative;font-family:'Montserrat',sans-serif}
  .banner{position:absolute;left:184px;top:184px;width:832px;height:2277px;display:block}
  .title{font-family:'Montserrat',sans-serif;font-weight:800;fill:var(--aqua-title);text-anchor:middle}
  .step-num{font-family:'Montserrat',sans-serif;font-weight:700;fill:var(--white);font-size:27px}
  .step-head{font-family:'Montserrat',sans-serif;font-weight:700;fill:var(--white);font-size:18px}
  .step-body{font-family:'Montserrat',sans-serif;font-weight:500;fill:var(--white);font-size:7.4px}
  .icon{fill:none;stroke:var(--white);stroke-width:2;stroke-linejoin:round;stroke-linecap:round}
</style>
</head>
<body>
<svg class="banner" viewBox="139 139 629 1721" xmlns="http://www.w3.org/2000/svg" role="img" aria-label="Exit strategy plan infographic">
  <defs>
    <radialGradient id="paperGlow" cx="0.5" cy="0.45" r="0.7">
      <stop offset="0" stop-color="#ffffff"/>
      <stop offset="1" stop-color="#e4e7ea"/>
    </radialGradient>
    <symbol id="icon-store" viewBox="-40 -40 80 80">
      <g class="icon">
        <path d="M-30 -28 H30 L36 -12 H-36 Z"/>
        <path d="M-36 -12 q6 8 12 0 q6 8 12 0 q6 8 12 0 q6 8 12 0 q6 8 12 0 q6 8 12 0"/>
        <path d="M-24 -28 L-28 -12 M-12 -28 L-14 -12 M0 -28 V-12 M12 -28 L14 -12 M24 -28 L28 -12"/>
        <path d="M-32 -6 V34 H32 V-6"/>
        <rect x="-26" y="4" width="18" height="30"/>
        <rect x="0" y="4" width="24" height="18"/>
        <path d="M-26 18 H-8 M0 26 H24"/>
      </g>
    </symbol>
    <symbol id="icon-building" viewBox="-40 -40 80 80">
      <g class="icon">
        <rect x="-20" y="-36" width="40" height="72"/>
        <path d="M-34 -14 H-20 V36 H-34 Z M20 -20 H34 V36 H20"/>
        <rect x="-14" y="-30" width="7" height="7"/><rect x="-3.5" y="-30" width="7" height="7"/><rect x="7" y="-30" width="7" height="7"/>
        <rect x="-14" y="-18" width="7" height="7"/><rect x="-3.5" y="-18" width="7" height="7"/><rect x="7" y="-18" width="7" height="7"/>
        <rect x="-14" y="-6" width="7" height="7"/><rect x="-3.5" y="-6" width="7" height="7"/><rect x="7" y="-6" width="7" height="7"/>
        <rect x="-14" y="6" width="7" height="7"/><rect x="-3.5" y="6" width="7" height="7"/><rect x="7" y="6" width="7" height="7"/>
        <rect x="-7" y="22" width="14" height="14"/>
        <path d="M0 22 V36 M-30 -6 h6 M-30 4 h6 M-30 14 h6 M-30 24 h6 M24 -12 h6 M24 -2 h6 M24 8 h6 M24 18 h6 M24 28 h6"/>
      </g>
    </symbol>
    <symbol id="icon-cafe" viewBox="-40 -40 80 80">
      <g class="icon">
        <path d="M-34 -8 Q-30 -34 0 -36 Q30 -34 34 -8 Q28 -14 23 -8 Q17 -14 12 -8 Q6 -14 0 -8 Q-6 -14 -12 -8 Q-17 -14 -23 -8 Q-28 -14 -34 -8 Z"/>
        <path d="M0 -36 Q-12 -24 -12 -8 M0 -36 Q12 -24 12 -8 M-23 -8 Q-22 -26 0 -36 M23 -8 Q22 -26 0 -36"/>
        <path d="M0 -8 V14"/>
        <path d="M-18 14 H18 M-14 14 L10 36 M14 14 L-10 36"/>
        <path d="M-34 4 V36 M-34 22 H-22 V36 M34 4 V36 M34 22 H22 V36"/>
      </g>
    </symbol>
  </defs>

  <rect class="paper" x="139" y="139" width="629" height="1721" fill="url(#paperGlow)"/>
  <g opacity="0.35" stroke="var(--paper-edge)" stroke-width="1" fill="none">
    <path d="M139 700 L768 1300 M139 1100 L768 1700 M139 1500 L500 1860 M768 700 L139 1300 M768 1100 L139 1700 M768 1500 L400 1860"/>
  </g>

  <path d="M139 139 H768 V425 Q453 540 139 425 Z" fill="var(--aqua)"/>
  <path d="M139 139 H768 V412 Q453 528 139 412 Z" fill="var(--navy)"/>
  <text class="title" x="453" y="262" font-size="97">EXIT</text>
  <text class="title" x="453" y="346" font-size="97">STRATEGY</text>
  <text class="title" x="453" y="431" font-size="97">PLAN</text>

  <polygon points="355,677 680,677 560,722 255,722" fill="var(--navy)"/>
  <polygon points="570,845 300,845 255,889 640,889" fill="var(--navy)"/>
  <polygon points="235,1242 540,1242 650,1287 330,1287" fill="var(--navy)"/>
  <polygon points="330,1411 560,1411 620,1454 220,1454" fill="var(--navy)"/>
  <polygon points="235,1582 540,1582 650,1625 330,1625" fill="var(--navy)"/>

  <!-- Step A1 -->
  <g class="step">
    <rect x="240" y="551" width="474" height="126" rx="63" fill="var(--aqua)"/>
    <circle cx="270" cy="610" r="88" fill="var(--aqua-soft)"/>
    <circle cx="277" cy="615" r="80" fill="var(--aqua)"/>
    <circle cx="277" cy="615" r="71" fill="var(--navy)"/>
    <use href="#icon-store" x="237" y="575" width="80" height="80"/>
    <text x="371" y="598"><tspan class="step-num">01</tspan><tspan class="step-head" dx="3">YOUT TEXT HERE</tspan></text>
    <text class="step-body" x="371" y="618">Lorem ipsum dolor sit amet, conse ctetur adipiscing elit, sed do</text>
    <text class="step-body" x="371" y="628">eiu smod tempor incididunt ut labore et dolore magna aliqua.</text>
    <circle cx="380" cy="646" r="7.5" fill="var(--navy)"/><circle cx="405" cy="646" r="7.5" fill="var(--navy)"/>
    <circle cx="430" cy="646" r="7.5" fill="var(--white)"/><circle cx="455" cy="646" r="7.5" fill="var(--white)"/>
    <circle cx="480" cy="646" r="7.5" fill="var(--aqua-soft)"/><circle cx="505" cy="646" r="7.5" fill="var(--aqua-soft)"/>
  </g>

  <!-- Step A2 -->
  <g class="step">
    <rect x="205" y="720" width="470" height="126" rx="63" fill="var(--aqua)"/>
    <circle cx="637" cy="782" r="88" fill="var(--aqua-soft)"/>
    <circle cx="629" cy="782" r="80" fill="var(--aqua)"/>
    <circle cx="629" cy="782" r="71" fill="var(--navy)"/>
    <use href="#icon-building" x="589" y="742" width="80" height="80"/>
    <text x="541" y="768" text-anchor="end"><tspan class="step-head">YOUT TEXT HERE</tspan><tspan class="step-num" dx="6">02</tspan></text>
    <text class="step-body" x="533" y="788" text-anchor="end">Lorem ipsum dolor sit amet, conse ctetur adipiscing elit, sed do</text>
    <text class="step-body" x="533" y="798" text-anchor="end">eiu smod tempor incididunt ut labore et dolore magna aliqua.</text>
    <circle cx="401" cy="816" r="7.5" fill="var(--aqua-soft)"/><circle cx="426" cy="816" r="7.5" fill="var(--aqua-soft)"/>
    <circle cx="451" cy="816" r="7.5" fill="var(--slate)"/><circle cx="476" cy="816" r="7.5" fill="var(--slate)"/>
    <circle cx="501" cy="816" r="7.5" fill="var(--navy)"/><circle cx="526" cy="816" r="7.5" fill="var(--navy)"/>
  </g>

  <!-- Step A3 -->
  <g class="step">
    <rect x="240" y="887" width="474" height="126" rx="63" fill="var(--aqua)"/>
    <circle cx="270" cy="945" r="88" fill="var(--aqua-soft)"/>
    <circle cx="277" cy="950" r="80" fill="var(--aqua)"/>
    <circle cx="277" cy="950" r="71" fill="var(--navy)"/>
    <use href="#icon-cafe" x="237" y="910" width="80" height="80"/>
    <text x="371" y="939"><tspan class="step-num">03</tspan><tspan class="step-head" dx="3">YOUT TEXT HERE</tspan></text>
    <text class="step-body" x="371" y="959">Lorem ipsum dolor sit amet, conse ctetur adipiscing elit, sed do</text>
    <text class="step-body" x="371" y="969">eiu smod tempor incididunt ut labore et dolore magna aliqua.</text>
    <circle cx="380" cy="987" r="7.5" fill="var(--navy)"/><circle cx="405" cy="987" r="7.5" fill="var(--navy)"/>
    <circle cx="430" cy="987" r="7.5" fill="var(--navy)"/><circle cx="455" cy="987" r="7.5" fill="var(--slate)"/>
    <circle cx="480" cy="987" r="7.5" fill="var(--slate)"/><circle cx="505" cy="987" r="7.5" fill="var(--slate-light)"/>
  </g>

  <!-- Step B1 -->
  <g class="step">
    <rect x="190" y="1116" width="470" height="126" rx="63" fill="var(--aqua)"/>
    <circle cx="636" cy="1172" r="88" fill="var(--aqua-soft)"/>
    <circle cx="628" cy="1178" r="80" fill="var(--aqua)"/>
    <circle cx="628" cy="1178" r="71" fill="var(--navy)"/>
    <use href="#icon-store" x="588" y="1138" width="80" height="80"/>
    <text x="537" y="1163" text-anchor="end"><tspan class="step-head">YOUT TEXT HERE</tspan><tspan class="step-num" dx="6">01</tspan></text>
    <text class="step-body" x="534" y="1183" text-anchor="end">Lorem ipsum dolor sit amet, conse ctetur adipiscing elit, sed do</text>
    <text class="step-body" x="524" y="1193" text-anchor="end">eiu smod tempor incididunt ut labore et dolore magna aliqua.</text>
    <circle cx="400" cy="1211" r="7.5" fill="var(--aqua-soft)"/><circle cx="425" cy="1211" r="7.5" fill="var(--aqua-soft)"/>
    <circle cx="450" cy="1211" r="7.5" fill="var(--white)"/><circle cx="475" cy="1211" r="7.5" fill="var(--white)"/>
    <circle cx="500" cy="1211" r="7.5" fill="var(--navy)"/><circle cx="525" cy="1211" r="7.5" fill="var(--navy)"/>
  </g>

  <!-- Step B2 -->
  <g class="step">
    <rect x="240" y="1285" width="458" height="126" rx="63" fill="var(--aqua)"/>
    <circle cx="269" cy="1342" r="88" fill="var(--aqua-soft)"/>
    <circle cx="276" cy="1347" r="80" fill="var(--aqua)"/>
    <circle cx="276" cy="1347" r="71" fill="var(--navy)"/>
    <use href="#icon-building" x="236" y="1307" width="80" height="80"/>
    <text x="369" y="1333"><tspan class="step-num">02</tspan><tspan class="step-head" dx="8">YOUT TEXT HERE</tspan></text>
    <text class="step-body" x="371" y="1353">Lorem ipsum dolor sit amet, conse ctetur adipiscing elit, sed do</text>
    <text class="step-body" x="382" y="1363">eiu smod tempor incididunt ut labore et dolore magna aliqua.</text>
    <circle cx="379" cy="1381" r="7.5" fill="var(--navy)"/><circle cx="404" cy="1381" r="7.5" fill="var(--navy)"/>
    <circle cx="429" cy="1381" r="7.5" fill="var(--slate)"/><circle cx="454" cy="1381" r="7.5" fill="var(--slate)"/>
    <circle cx="479" cy="1381" r="7.5" fill="var(--aqua-soft)"/><circle cx="504" cy="1381" r="7.5" fill="var(--aqua-soft)"/>
  </g>

  <!-- Step B3 -->
  <g class="step">
    <rect x="190" y="1453" width="470" height="128" rx="64" fill="var(--aqua)"/>
    <circle cx="636" cy="1511" r="88" fill="var(--aqua-soft)"/>
    <circle cx="628" cy="1517" r="80" fill="var(--aqua)"/>
    <circle cx="628" cy="1517" r="71" fill="var(--navy)"/>
    <use href="#icon-store" x="588" y="1477" width="80" height="80"/>
    <text x="540" y="1502" text-anchor="end"><tspan class="step-head">YOUT TEXT HERE</tspan><tspan class="step-num" dx="6">03</tspan></text>
    <text class="step-body" x="534" y="1522" text-anchor="end">Lorem ipsum dolor sit amet, conse ctetur adipiscing elit, sed do</text>
    <text class="step-body" x="524" y="1532" text-anchor="end">eiu smod tempor incididunt ut labore et dolore magna aliqua.</text>
    <circle cx="400" cy="1550" r="7.5" fill="var(--aqua-soft)"/><circle cx="425" cy="1550" r="7.5" fill="var(--aqua-soft)"/>
    <circle cx="450" cy="1550" r="7.5" fill="var(--white)"/><circle cx="475" cy="1550" r="7.5" fill="var(--white)"/>
    <circle cx="500" cy="1550" r="7.5" fill="var(--navy)"/><circle cx="525" cy="1550" r="7.5" fill="var(--navy)"/>
  </g>

  <!-- Step B4 -->
  <g class="step">
    <rect x="240" y="1623" width="458" height="126" rx="63" fill="var(--aqua)"/>
    <circle cx="269" cy="1681" r="88" fill="var(--aqua-soft)"/>
    <circle cx="276" cy="1686" r="80" fill="var(--aqua)"/>
    <circle cx="276" cy="1686" r="71" fill="var(--navy)"/>
    <use href="#icon-building" x="236" y="1646" width="80" height="80"/>
    <text x="371" y="1672"><tspan class="step-num">04</tspan><tspan class="step-head" dx="12">YOUT TEXT HERE</tspan></text>
    <text class="step-body" x="371" y="1692">Lorem ipsum dolor sit amet, conse ctetur adipiscing elit, sed do</text>
    <text class="step-body" x="382" y="1702">eiu smod tempor incididunt ut labore et dolore magna aliqua.</text>
    <circle cx="379" cy="1720" r="7.5" fill="var(--navy)"/><circle cx="404" cy="1720" r="7.5" fill="var(--navy)"/>
    <circle cx="429" cy="1720" r="7.5" fill="var(--slate)"/><circle cx="454" cy="1720" r="7.5" fill="var(--slate)"/>
    <circle cx="479" cy="1720" r="7.5" fill="var(--aqua-soft)"/><circle cx="504" cy="1720" r="7.5" fill="var(--aqua-soft)"/>
  </g>
</svg>
</body>
</html>
```